I need a business card design for a new company that will be doing consulting work around issues of cultural competency, and diversity and inclusion. I would like the design to be crisp and clear with bold but conservative colors and incorporate shades of blue

Target Market(s)

Small businesses, schools, non-profits

Industry/Entity Type

Consulting

Font styles to use
Serif
Sans Serif

Colors
0c5ba6
6b449b
3276b5
0292cd

Requirements
Must have
• A Morrow Venture (name of company)
• Lemlem Tavish
• CEO
• lemlem@amorrowventure.com
• (215)483-2756

```html
<!DOCTYPE html>
<html lang="en">
<head>
<meta charset="utf-8">
<title>A Morrow Venture — Business Card</title>
<link rel="stylesheet" href="https://fonts.googleapis.com/css2?family=Jost:wght@700&family=Poppins:wght@400;500;700&display=swap">
<style>
  :root {
    --backdrop: #6e6e6e;
    --card-blue: #1f5cb2;
    --card-blue-light: #2a6cc4;
    --card-blue-deep: #184d9c;
    --band-navy: #1b3e84;
    --band-navy-dark: #163470;
    --rule: #c9d8f0;
    --text-white: #ffffff;
    --icon-ink: #1f5cb2;
  }
  html, body {
    margin: 0;
    width: 1200px;
    height: 1200px;
    overflow: hidden;
    background: var(--backdrop);
  }
  .canvas {
    position: relative;
    width: 1200px;
    height: 1200px;
  }
  .card {
    position: absolute;
    left: 105px;
    top: 300px;
    width: 990px;
    height: 600px;
    background: radial-gradient(ellipse at 50% 40%, var(--card-blue-light), var(--card-blue) 55%, var(--card-blue-deep));
    box-shadow: 0 6px 18px rgba(0,0,0,0.35);
    overflow: hidden;
    color: var(--text-white);
  }
  .company-name {
    position: absolute;
    top: 82px;
    left: 0;
    width: 100%;
    margin: 0;
    text-align: center;
    font-family: "Jost", sans-serif;
    font-weight: 700;
    font-size: 54px;
    letter-spacing: 0.5px;
    line-height: 1;
    text-shadow: 0 3px 4px rgba(0,0,0,0.45);
  }
  .name-band {
    position: absolute;
    left: 0;
    top: 228px;
    width: 100%;
    height: 144px;
    background: linear-gradient(180deg, var(--band-navy-dark), var(--band-navy) 40%, var(--band-navy));
    border-top: 2px solid var(--rule);
    border-bottom: 2px solid var(--rule);
    box-shadow: 0 14px 22px -10px rgba(0,0,0,0.55), 0 -10px 18px -10px rgba(0,0,0,0.5);
    text-align: center;
  }
  .person-name {
    margin: 22px 0 0;
    font-family: "Poppins", sans-serif;
    font-weight: 400;
    font-size: 44px;
    line-height: 1.1;
    text-shadow: 0 2px 3px rgba(0,0,0,0.4);
  }
  .person-name .given { font-weight: 700; }
  .person-title {
    margin: 4px 0 0;
    font-family: "Poppins", sans-serif;
    font-weight: 500;
    font-size: 28px;
    letter-spacing: 5px;
    line-height: 1.2;
  }
  .contact {
    position: absolute;
    top: 440px;
    width: 460px;
    text-align: center;
    font-family: "Poppins", sans-serif;
    font-size: 28px;
    line-height: 1;
  }
  .contact--phone { left: 41px; }
  .contact--email { left: 493px; }
  .contact-icon {
    display: block;
    margin: 0 auto 28px;
    width: 40px;
    height: 40px;
  }
</style>
</head>
<body>
<main class="canvas">
  <section class="card">
    <h1 class="company-name">A MORROW VENTURE</h1>
    <div class="name-band">
      <p class="person-name"><span class="given">LEMLEM</span> TAVISH</p>
      <p class="person-title">CEO</p>
    </div>
    <div class="contact contact--phone">
      <svg class="contact-icon" viewBox="0 0 40 40" aria-hidden="true">
        <circle cx="20" cy="20" r="19" fill="#ffffff"/>
        <rect x="14" y="9" width="12" height="22" rx="2" fill="none" stroke="#1f5cb2" stroke-width="2.2"/>
        <circle cx="20" cy="27" r="1.4" fill="#1f5cb2"/>
      </svg>
      <span>(215)483-2756</span>
    </div>
    <div class="contact contact--email">
      <svg class="contact-icon" viewBox="0 0 40 40" aria-hidden="true">
        <circle cx="20" cy="20" r="19" fill="#ffffff"/>
        <rect x="10" y="13" width="20" height="14" rx="1.5" fill="none" stroke="#1f5cb2" stroke-width="2.2"/>
        <path d="M10.5 14 L20 21.5 L29.5 14" fill="none" stroke="#1f5cb2" stroke-width="2.2"/>
      </svg>
      <span>lemlem@amorrowventure.com</span>
    </div>
  </section>
</main>
</body>
</html>
```